Vorna Fleet business card

I am needing a business card that at a glance shows all the services that we provide emphasizing some more than others. We are a Fleet and Compliance management company as well as a software company. We provide outsourced solutions for KPX compliance and HR services via our own software.
In addition, we do
drug testing
GPS
Cameras
Electronic DVIRS
ELD's

Target Market(s)

Transportation company owners

Industry/Entity Type

Transportation supplier

Contact Information for Business Card

the card should inform potential customers what we do

Other font styles liked:
• I have added brand guidelines. See attached

Requirements
Must have
• See description
Should not have
• Colors outside my brand guide. See attached

```html
<!DOCTYPE html>
<html lang="en">
<head>
<meta charset="utf-8">
<title>Vorna Fleet business card</title>
<link href="https://fonts.googleapis.com/css2?family=Open+Sans:wght@400;800&family=PT+Sans:wght@400&display=swap" rel="stylesheet">
<style>
  :root {
    --brand-red: #b8212f;
    --ink: #1d1d1b;
    --paper: #ffffff;
    --rule: #8c8c8c;
    --stage: #3a3a3a;
  }
  * { margin: 0; padding: 0; box-sizing: border-box; }
  html, body { width: 1200px; height: 582px; overflow: hidden; }
  body { background: var(--stage); position: relative; font-family: "PT Sans", sans-serif; }

  .card {
    position: absolute;
    width: 478px;
    height: 287px;
    overflow: hidden;
    box-shadow: 0 8px 18px rgba(0,0,0,0.45);
  }
  .card--front { left: 92px; top: 147px; background: var(--brand-red); }
  .card--back { left: 631px; top: 149px; background: var(--paper); }

  .wordmark {
    position: absolute;
    font-family: "Open Sans", sans-serif;
    font-weight: 800;
    letter-spacing: -0.5px;
    white-space: nowrap;
  }
  .card--front .wordmark {
    left: 0; right: 0; top: 112px;
    text-align: center;
    font-size: 44px;
    line-height: 1;
    color: var(--paper);
  }
  .card--back .wordmark {
    right: 34px; top: 186px;
    font-size: 25px;
    line-height: 1;
    color: var(--ink);
  }

  .stripe { position: absolute; left: 0; right: 0; }
  .card--front .stripe--dark { top: 249px; height: 4px; background: var(--ink); }
  .card--front .stripe--light { top: 257px; height: 6px; background: var(--paper); }
  .card--back .stripe--dark { top: 249px; height: 4px; background: var(--ink); }
  .card--back .stripe--accent { top: 257px; height: 6px; background: var(--brand-red); }

  .services { position: absolute; left: 0; top: 0; width: 100%; list-style: none; }
  .service {
    position: absolute;
    font-size: 12.5px;
    line-height: 1;
    color: var(--ink);
    text-transform: uppercase;
    white-space: nowrap;
  }
  .service svg { position: absolute; left: -18px; top: -2px; width: 9px; height: 9px; }
  .rule { position: absolute; left: 41px; width: 396px; height: 1px; background: var(--rule); }
</style>
</head>
<body>

  <section class="card card--front" aria-label="Card front">
    <span class="wordmark">Vorna Fleet</span>
    <div class="stripe stripe--dark"></div>
    <div class="stripe stripe--light"></div>
  </section>

  <section class="card card--back" aria-label="Card back">
    <ul class="services">
      <li class="service" style="left:74px;top:51px"><svg viewBox="0 0 10 10"><path d="M1 5.5 L3.8 8.5 L9 1" fill="none" stroke="var(--brand-red)" stroke-width="1.4"/></svg>Solutions for KPX compliance</li>
      <li class="service" style="left:329px;top:51px"><svg viewBox="0 0 10 10"><path d="M1 5.5 L3.8 8.5 L9 1" fill="none" stroke="var(--brand-red)" stroke-width="1.4"/></svg>Drug testing</li>
      <li class="service" style="left:74px;top:83px"><svg viewBox="0 0 10 10"><path d="M1 5.5 L3.8 8.5 L9 1" fill="none" stroke="var(--brand-red)" stroke-width="1.4"/></svg>HR services via our own software</li>
      <li class="service" style="left:329px;top:83px"><svg viewBox="0 0 10 10"><path d="M1 5.5 L3.8 8.5 L9 1" fill="none" stroke="var(--brand-red)" stroke-width="1.4"/></svg>GPS</li>
      <li class="service" style="left:74px;top:115px"><svg viewBox="0 0 10 10"><path d="M1 5.5 L3.8 8.5 L9 1" fill="none" stroke="var(--brand-red)" stroke-width="1.4"/></svg>Cameras</li>
      <li class="service" style="left:329px;top:115px"><svg viewBox="0 0 10 10"><path d="M1 5.5 L3.8 8.5 L9 1" fill="none" stroke="var(--brand-red)" stroke-width="1.4"/></svg>Electronic DVIRS</li>
      <li class="service" style="left:74px;top:147px"><svg viewBox="0 0 10 10"><path d="M1 5.5 L3.8 8.5 L9 1" fill="none" stroke="var(--brand-red)" stroke-width="1.4"/></svg>ELD's</li>
    </ul>
    <div class="rule" style="top:73px"></div>
    <div class="rule" style="top:107px"></div>
    <div class="rule" style="top:140px"></div>
    <span class="wordmark">Vorna Fleet</span>
    <div class="stripe stripe--dark"></div>
    <div class="stripe stripe--accent"></div>
  </section>

</body>
</html>
```